Bright Nova Works

We need a professional letter head format for our company. Now we have a logo but need to desing a new logo also. I have uploaded our old logo. Use the color in the logo and design a new one.

Dear Designers , Need to mention "BNW" and please dont use our old LOGO. we need a new catchy one.

```html
<!DOCTYPE html>
<html lang="en">
<head>
<meta charset="utf-8">
<title>Bright Nova Works – Letterhead</title>
<link rel="stylesheet" href="https://fonts.googleapis.com/css2?family=Open+Sans:wght@400;600&family=Lato:wght@400;700&display=swap">
<style>
  :root {
    --navy: #142c47;
    --green: #97c13c;
    --ink: #3a3a3a;
    --muted: #555;
    --rule: #b9c4cf;
    --paper: #ffffff;
    --backdrop: #e6e6e6;
  }
  * { margin: 0; padding: 0; box-sizing: border-box; }
  html, body { width: 1040px; height: 1200px; overflow: hidden; background: var(--backdrop); }
  .letterhead {
    position: absolute; left: 77px; top: 30px;
    width: 885px; height: 1140px;
    background: var(--paper);
    font-family: "Open Sans", sans-serif; color: var(--ink);
    box-shadow: 0 2px 10px rgba(0,0,0,.12);
    overflow: hidden;
  }
  .frame { position: absolute; inset: 0; width: 100%; height: 100%; }
  .brand {
    position: absolute; right: 65px; top: 176px;
    display: flex; align-items: center; gap: 10px;
    font-family: "Lato", sans-serif; font-weight: 700; font-size: 31px;
    color: var(--navy); letter-spacing: .5px;
  }
  .brand-mark { width: 16px; height: 16px; background: var(--green); }
  .letter { position: absolute; left: 83px; width: 714px; font-size: 14px; }
  .issue-date { top: 236px; }
  .recipient { top: 270px; line-height: 17px; }
  .salutation { top: 366px; }
  .body-text { top: 414px; line-height: 25.8px; text-align: justify; }
  .body-text p + p { margin-top: 25.8px; }
  .closing { top: 801px; }
  .signatory { top: 874px; }
  .signatory-name { font-size: 17px; font-weight: 600; color: #333; }
  .signatory-role { font-size: 14px; color: var(--muted); margin-top: 3px; }
  .footer {
    position: absolute; left: 150px; width: 583px; top: 1043px;
    font-family: "Lato", sans-serif; font-size: 16px; color: #1a1a1a; text-align: center;
  }
  .footer-address { padding-bottom: 6px; border-bottom: 1px solid var(--rule); }
  .footer-contacts { display: flex; justify-content: space-between; margin-top: 6px; }
  .web-accent { color: var(--green); }
</style>
</head>
<body>
  <main class="letterhead">
    <svg class="frame" viewBox="0 0 789 1017" preserveAspectRatio="none" aria-hidden="true">
      <path d="M0 0 H214 C100 6 20 80 14 198 V1017 H0 Z" fill="var(--navy)"/>
      <path d="M772 0 H789 V1017 H519 C650 1005 760 960 772 858 Z" fill="var(--green)"/>
    </svg>

    <div class="brand"><span class="brand-mark"></span>Bright Nova Works</div>

    <p class="letter issue-date">Issuing Date: May 5, 2018</p>
    <div class="letter recipient">
      <p>Name Of Employee Mr. Halvorsen</p>
      <p>Address of Employee</p>
      <p>Address Line 2 etc..</p>
    </div>
    <p class="letter salutation">Dear Mr. Halvorsen</p>

    <div class="letter body-text">
      <p>Lorem Ipsum has been the industry's standard dummy text ever since the 1500s, when an unknown printer took a galley of type and scrambled it to make a type specimen book. It has survived not only five centuries, but also the leap into electronic typesetting, remaining essentially unchanged. It was popularised in the 1960s with the release of Typeleaf sheets containing Lorem Ipsum passages, and more recently with desktop publishing software like Norvik PageForge including versions of Lorem Ipsum.</p>
      <p>Lorem Ipsum is simply dummy text of the printing and typesetting industry. Lorem Ipsum has been the industry's standard dummy text ever since the 1500s, when an unknown printer took a galley of type and scrambled it to make a type specimen book.</p>
      <p>It has survived not only five centuries, but also the leap into electronic typesetting, remaining essentially unchanged. It was popularised in the 1960s with the release of Typeleaf sheets containing Lorem IpsumIpsum passages.</p>
    </div>

    <p class="letter closing">Yours Sincerely</p>
    <div class="letter signatory">
      <p class="signatory-name">Daniel Morrow</p>
      <p class="signatory-role">Managing Director</p>
    </div>

    <footer class="footer">
      <p class="footer-address">18 Lumen Street, 40217, Eastmoor</p>
      <p class="footer-contacts">
        <span>P: 021-555 0147</span><span class="sep">|</span>
        <span>E: hello@brightnova.example</span><span class="sep">|</span>
        <span>www.<span class="web-accent">brightnova</span>.example</span>
      </p>
    </footer>
  </main>
</body>
</html>
```